Business card design

Hi,
I need to have a business card design based on the current logo.
If competitive I not put it out to everyone.

It can be single of double sided

Target Market(s)

Food businesses

Industry/Entity Type

Food Manufacturing

Contact Information for Business Card

Details will on card will be as follows Name = Marcus Helt Email = Marcus@TalBakery.com.au Phone = 0418562207 Address = 17 Lanford Street , Fortitude Valley QLD 4006 Australia

Font styles to use
Other font styles liked:
• based on two fonts - Adelle & Museo

Requirements
Must have
• Based on the on switch concept

```html
<!DOCTYPE html>
<html lang="en">
<head>
<meta charset="utf-8">
<title>TalBakery Business Card – Marcus Helt</title>
<link href="https://fonts.googleapis.com/css2?family=Poppins:wght@500;600&family=Roboto+Slab:wght@400;500&display=swap" rel="stylesheet">
<style>
  :root {
    --backdrop: #dadada;
    --brand-red: #e2304d;
    --name-red: #dc3a3a;
    --paper: #f4f4f2;
    --ink: #3b2a2c;
  }
  html, body {
    margin: 0;
    padding: 0;
    width: 1200px;
    height: 960px;
    overflow: hidden;
    background: var(--backdrop);
  }
  .canvas {
    position: relative;
    width: 1200px;
    height: 960px;
  }
  .card {
    position: absolute;
    top: 126px;
    width: 400px;
    height: 700px;
  }
  .card svg { display: block; }
  .card--front { left: 168px; }
  .card--back { left: 644px; }
  .card-text {
    position: absolute;
    left: 0;
    width: 400px;
    text-align: center;
    font-family: "Poppins", sans-serif;
    color: var(--ink);
  }
  .holder-name {
    top: 186px;
    font-size: 21px;
    font-weight: 600;
    color: var(--name-red);
    letter-spacing: 0.2px;
  }
  .brand {
    top: 398px;
    left: 90px;
    width: 218px;
    display: flex;
    justify-content: flex-end;
    align-items: center;
    gap: 10px;
  }
  .brand-dot {
    width: 22px;
    height: 22px;
    border-radius: 50%;
    background: var(--brand-red);
  }
  .brand-name {
    font-size: 31px;
    font-weight: 500;
    color: var(--ink);
    line-height: 1;
    letter-spacing: 0.3px;
  }
  .tagline {
    top: 432px;
    left: 68px;
    width: 240px;
    text-align: right;
    font-family: "Roboto Slab", serif;
    font-size: 10px;
    font-weight: 500;
    color: var(--ink);
  }
  .address {
    top: 515px;
    font-size: 16px;
    font-weight: 500;
    line-height: 20px;
  }
  .contact {
    top: 604px;
    font-size: 16.5px;
    font-weight: 500;
    line-height: 24px;
  }
  .icon { position: absolute; }
</style>
</head>
<body>
<main class="canvas">

  <section class="card card--front" aria-label="Card front">
    <svg width="400" height="700" viewBox="0 0 400 700">
      <rect x="0" y="0" width="400" height="700" rx="200" fill="var(--brand-red)"/>
      <circle cx="200" cy="200" r="165" fill="var(--paper)"/>
      <circle cx="200" cy="200" r="110" fill="var(--brand-red)"/>
    </svg>
  </section>

  <section class="card card--back" aria-label="Card back">
    <svg width="400" height="700" viewBox="0 0 400 700">
      <rect x="0" y="0" width="400" height="700" rx="200" fill="var(--paper)"/>
      <circle cx="200" cy="200" r="165" fill="var(--brand-red)"/>
      <circle cx="200" cy="200" r="110" fill="var(--paper)"/>
    </svg>

    <div class="card-text holder-name">MARCUS HELT</div>

    <div class="card-text brand">
      <span class="brand-dot"></span>
      <span class="brand-name">TALBAKERY</span>
    </div>
    <div class="card-text tagline">Fresh Baking Every Day</div>

    <svg class="icon pin-icon" style="left:190px;top:480px" width="20" height="28" viewBox="0 0 20 28" aria-hidden="true">
      <path d="M10 1a8 8 0 0 0-8 8c0 6 8 13 8 13s8-7 8-13a8 8 0 0 0-8-8z" fill="var(--brand-red)"/>
      <circle cx="10" cy="9" r="3.2" fill="var(--paper)"/>
      <rect x="2" y="25" width="16" height="2" fill="var(--brand-red)"/>
    </svg>

    <div class="card-text address">17 Lanford Street ,<br>Harlow Vale<br>QLD 4178 Australia</div>

    <svg class="icon mail-icon" style="left:175px;top:579px" width="22" height="22" viewBox="0 0 22 22" aria-hidden="true">
      <circle cx="11" cy="11" r="11" fill="var(--brand-red)"/>
      <rect x="5.5" y="7" width="11" height="8" rx="1" fill="none" stroke="var(--paper)" stroke-width="1.6"/>
      <path d="M6 8l5 4 5-4" fill="none" stroke="var(--paper)" stroke-width="1.6"/>
    </svg>
    <svg class="icon phone-icon" style="left:203px;top:579px" width="22" height="22" viewBox="0 0 22 22" aria-hidden="true">
      <circle cx="11" cy="11" r="11" fill="var(--brand-red)"/>
      <path d="M7.5 6c.6-.4 1.2-.3 1.5.2l1 1.8c.3.5.1 1-.3 1.3l-.6.5c.5 1.1 1.4 2 2.5 2.5l.5-.6c.3-.4.8-.6 1.300-.3l1.8 1c.5.3.6.9.2 1.5-.7 1-1.8 1.5-3 1.1-2.6-.9-4.5-2.8-5.4-5.4-.4-1.2.1-2.3 1.1-3z" fill="var(--paper)"/>
    </svg>

    <div class="card-text contact">Marcus@TalBakery.com.au<br>(041) 856 2207</div>
  </section>

</main>
</body>
</html>
```